Project Management - Web Design Project

Vantrel 4 Management Limited is a company which provides specialist Project Control and Contract Management expertise to the Engineering, Construction and Manufacturing industries. The emphasis is on advanced Project Management techniques in particular Planning & Scheduling, Cost Control, Change Control, Risk Management, Reporting and Contract Administration. We are a global company (albeit a small start-up at this time) and pride ourselves on our ability to support projects to help them achieve their goals and objectives. Our aim is to implement work class control tools in a simple and user friendly manner. We would like the website to appear professional but at the same time easy to navigate and a good balance between text and pictures. The final design should communicate our value added service to our customers, our willingness to support and our structured approach to our work.

Target Market(s)

Project Management professionals working for engineering, construction and manufacturing organisations involved with delivering projects.

Industry/Entity Type

Construction

Requirements
Must have
• The website must include all of the content from the attached Excel brief. The company logo (attached) must also be included in the design. The design must portray a professional look and feel. Please include pictures and photographs related to project management in the engineering, construction and manufacturing industries. We may supplement with pictures of our own during the next steps.
Nice to have
• Emphasis that Vantrel 4 is available to support, guide, direct to achieve positive outcomes for the projects. We work hard at developing our customer relationships. Our employees are experienced in advanced project management techniques.
Should not have
• The design should not use old style fonts. It should look modern and professional. Do not include cartoons or silly illustrations.

```html
<!DOCTYPE html>
<html lang="en">
<head>
<meta charset="utf-8">
<title>Vantrel 4 Management Limited</title>
<link href="https://fonts.googleapis.com/css2?family=Exo+2:ital,wght@0,300;0,400;1,400;1,500&family=Michroma&family=Arimo:wght@400;700&display=swap" rel="stylesheet">
<style>
:root{
  --page-top:#f3f4f6;
  --page-bottom:#e2e4e7;
  --panel:#f4f5f6;
  --panel-edge:#dcdfe2;
  --text:#6d6f73;
  --brand:#66696e;
  --blue:#1a63b8;
  --nav-bg:#c7dcee;
  --nav-text:#55606b;
  --footer:#6b6b6b;
  --footer-dark:#5a5a5a;
  --red:#c8281e;
  --white:#ffffff;
}
*{margin:0;padding:0;box-sizing:border-box}
html,body{width:1200px;height:1136px;overflow:hidden}
body{
  position:relative;
  background:linear-gradient(var(--page-top),var(--page-bottom) 60%,#ececec);
  font-family:"Arimo",Arial,sans-serif;color:var(--text);
}
.abs{position:absolute}
ul{list-style:none}

/* header */
.brand{left:178px;top:112px;display:flex;align-items:flex-start;gap:10px;color:var(--brand);font-family:"Arimo",sans-serif;font-weight:400}
.brand-square{width:16px;height:16px;background:var(--blue);margin-top:8px;flex:none}
.brand-name{line-height:1}
.brand-name .big{display:block;font-size:30px;letter-spacing:1px}
.brand-name .small{display:block;font-size:12px;letter-spacing:2.6px;margin-top:6px;text-transform:uppercase}
.top-links{left:852px;top:45px;font-family:"Exo 2",sans-serif;font-size:13px;color:#555;display:flex;gap:18px}
.top-links span{display:flex;align-items:center;gap:4px}
.social{top:112px;left:840px;display:flex;gap:14px;font-size:11px;color:#555}
.social span{display:flex;align-items:center;gap:4px}
.social i{display:block;width:9px;height:9px;background:#2f74c2}

/* nav */
.main-nav{left:170px;top:170px;width:858px;height:35px;background:var(--nav-bg);
  display:flex;justify-content:space-around;align-items:center;
  font-family:"Michroma",sans-serif;font-size:9.6px;color:var(--nav-text);letter-spacing:.4px;border:1px solid #b9cfe2}
.hero{left:170px;top:206px;width:858px;height:294px;
  background:linear-gradient(100deg,#5d6570 0%,#a9aeb5 35%,#d7dade 65%,#eef0f2 100%)}

/* panels */
.panel{background:var(--panel);border:1px solid var(--panel-edge)}
.left-panel{left:170px;top:502px;width:589px;height:500px}
.right-panel{left:767px;top:502px;width:261px;height:500px}
.welcome-title{left:187px;top:518px;font-family:"Exo 2",sans-serif;font-weight:300;font-size:24px;color:#5c5e62}
.welcome-title b{font-weight:400;color:var(--blue)}
.intro{left:187px;top:549px;width:554px;font-size:11.2px;line-height:16.3px;text-align:justify;letter-spacing:.2px}
.view{font-family:"Exo 2",sans-serif;font-size:10px;color:var(--red)}
.section-title{font-family:"Exo 2",sans-serif;font-style:italic;font-weight:500;font-size:15.5px;color:var(--blue);letter-spacing:.3px}
.box{background:#f8f8f8;border:1px solid #e1e3e5;border-radius:7px;box-shadow:0 1px 3px rgba(0,0,0,.08)}
.thumb{border:1px solid #c5c8cc}
.svc-list li{font-size:11px;font-weight:700;color:#6a6c70;height:19px;display:flex;align-items:center;gap:6px}
.doc{width:7px;height:9px;border:1px solid #4a86c8;background:#eaf2fb;flex:none}

/* right column */
.ref-title{left:777px;top:522px;font-family:"Exo 2",sans-serif;font-style:italic;font-size:16px;color:#6a6c70;letter-spacing:.6px}
.ref-cat{font-family:"Exo 2",sans-serif;font-style:italic;font-weight:500;font-size:12.5px;color:var(--blue)}
.ref-list li{font-size:11.5px;color:#6a6c70;height:18px;display:flex;align-items:center;gap:6px}
.dots{left:788px;width:210px;border-top:1px dotted #9a9da1}
.badges{left:777px;top:866px;width:239px;height:116px;background:var(--white);border:1px solid #d8dbde;padding:4px;
  display:grid;grid-template-columns:1fr 1fr;gap:6px}
.badges span{background:#f6f6f6;display:flex;align-items:center;justify-content:center}
.badges i{display:block;width:60px;height:22px;border-radius:4px}

/* footer */
.footer{left:0;top:1004px;width:1200px;height:108px;background:var(--footer)}
.footer-line{left:0;top:1112px;width:1200px;height:1px;background:#9a9a9a}
.footer-base{left:0;top:1113px;width:1200px;height:18px;background:var(--footer-dark)}
.footer-nav{left:0;top:1014px;width:1200px;display:flex;justify-content:center;gap:17px;font-size:9.5px;color:var(--white)}
.copyright{left:0;top:1091px;width:1200px;text-align:center;font-family:"Exo 2",sans-serif;font-size:10px;color:#e4e4e4}
</style>
</head>
<body>

<header>
  <div class="abs brand">
    <span class="brand-square"></span>
    <div class="brand-name"><span class="big">Vantrel 4</span><span class="small">Management Limited</span></div>
  </div>

  <div class="abs top-links">
    <span><svg width="12" height="11" viewBox="0 0 12 11"><path d="M1 6 6 1l5 5M3 5v5h6V5" fill="none" stroke="#c8281e" stroke-width="1.4"/></svg>HOME</span>
    <span><svg width="14" height="10" viewBox="0 0 14 10"><rect x=".5" y=".5" width="13" height="9" fill="#eaf2fb" stroke="#5a8fcc"/><path d="M.5 .5 7 6l6.5-5.5" fill="none" stroke="#5a8fcc"/></svg>CONTACT US</span>
  </div>

  <div class="abs social"><span><i></i>Facet</span><span><i></i>Chirp</span><span><i></i>Vidly</span><span><i></i>Linka</span></div>

  <nav class="abs main-nav">
    <span>ABOUT US</span><span>INTRODUCTION</span><span>PROJECT CONTROL</span><span>CONTRACT MANAGEMENT</span><span>SPECIALIST SERVICES</span><span>PROJECTS</span>
  </nav>
  <div class="abs hero" role="img" aria-label="Photo of three colleagues reviewing work on a laptop in a bright office"></div>
</header>

<main>
  <div class="abs panel left-panel"></div>
  <h1 class="abs welcome-title">Welcome to Vantrel<b>4</b> Management Limited</h1>
  <p class="abs intro">Vantrel 4 Management Limited provide project control and contract management expertise to the Engineering / Construction and Manufacturing industries. We are able to draw from the vast experience of our specialist resource base. Our employees have considerable experience gained from direct involvement on numerous large scale international projects. These projects include Civil, Building, Infrastructure and Defense with particular focus on the Rail and Aviation transportation sectors. Our employees possess the practical experience necessary to implement world class Project Control / Project Management systems and processes..</p>
  <span class="abs view" style="left:691px;top:661px">View details</span>

  <h2 class="abs section-title" style="left:191px;top:685px">Control Systems We Provide by Discipline:</h2>
  <div class="abs box" style="left:191px;top:710px;width:551px;height:117px"></div>
  <div class="abs thumb" style="left:199px;top:722px;width:114px;height:92px;background:linear-gradient(135deg,#8fa3bb,#dfe5ec)" role="img" aria-label="Photo of a businesswoman ticking off a checklist"></div>
  <ul class="abs svc-list" style="left:327px;top:721px">
    <li><i class="doc"></i>General</li><li><i class="doc"></i>Schedule</li><li><i class="doc"></i>ControlReporting</li><li><i class="doc"></i>Material / Sub Contract Control</li><li><i class="doc"></i>Reporting</li>
  </ul>
  <ul class="abs svc-list" style="left:526px;top:721px">
    <li><i class="doc"></i>Claim Analysis</li><li><i class="doc"></i>Change Control</li><li><i class="doc"></i>Risk &amp; Opportunity Management</li><li><i class="doc"></i>Governance</li>
  </ul>
  <span class="abs view" style="left:681px;top:803px">View details</span>

  <h2 class="abs section-title" style="left:191px;top:846px">Our Specialist Services:</h2>
  <div class="abs box" style="left:191px;top:870px;width:551px;height:118px"></div>
  <div class="abs thumb" style="left:199px;top:883px;width:114px;height:92px;background:linear-gradient(135deg,#9fb4c6,#e7edf2)" role="img" aria-label="Photo of a team meeting around a glass table"></div>
  <ul class="abs svc-list" style="left:327px;top:881px">
    <li><i class="doc"></i>Engineering Earned Value</li><li><i class="doc"></i>S-Curve Reporting</li><li><i class="doc"></i>Critical Issues Reporting</li><li><i class="doc"></i>Six Sigma</li><li><i class="doc"></i>Coaching / Mentoring / Training</li>
  </ul>
  <ul class="abs svc-list" style="left:529px;top:883px">
    <li><i class="doc"></i>Six Sigma</li><li><i class="doc"></i>Coaching / Mentoring / Training</li>
  </ul>
  <span class="abs view" style="left:681px;top:964px">View details</span>

  <aside>
    <div class="abs panel right-panel"></div>
    <h2 class="abs ref-title">Our reference projects:</h2>
    <h3 class="abs ref-cat" style="left:777px;top:556px">RAIL - PROJECTS</h3>
    <ul class="abs ref-list" style="left:784px;top:575px">
      <li><i class="doc"></i>Meridian Rapid Rail Link</li><li><i class="doc"></i>Harbour West Rail</li><li><i class="doc"></i>Midland Route Modernization</li><li><i class="doc"></i>Crossline Rail</li><li><i class="doc"></i>Riverside Line Extension Project</li>
    </ul>
    <div class="abs dots" style="top:674px"></div>
    <h3 class="abs ref-cat" style="left:775px;top:679px">AVIATION - PROJECTS</h3>
    <ul class="abs ref-list" style="left:784px;top:698px">
      <li><i class="doc"></i>New Coastal International Airport</li><li><i class="doc"></i>Lantern Bay International Airport</li>
    </ul>
    <div class="abs dots" style="top:744px"></div>
    <h3 class="abs ref-cat" style="left:777px;top:749px">MANUFACTURING - PROJECTS</h3>
    <ul class="abs ref-list" style="left:784px;top:767px">
      <li><i class="doc"></i>Alpine Twin-Deck Fleet</li>
    </ul>
    <div class="abs dots" style="top:793px"></div>
    <h3 class="abs ref-cat" style="left:777px;top:798px">BUILDING</h3>
    <ul class="abs ref-list" style="left:784px;top:817px">
      <li><i class="doc"></i>Arcadia Shopping Centre</li><li><i class="doc"></i>Northgate Head Office</li>
    </ul>
    <span class="abs view" style="left:961px;top:844px">View details</span>
    <div class="abs badges">
      <span><i style="background:#b79a52"></i></span>
      <span><i style="background:#c8281e"></i></span>
      <span><i style="background:#8a2a2a"></i></span>
      <span><i style="background:#8fd0c6"></i></span>
    </div>
  </aside>
</main>

<footer>
  <div class="abs footer"></div>
  <div class="abs footer-line"></div>
  <div class="abs footer-base"></div>
  <nav class="abs footer-nav">
    <span>HOME</span><span>ABOUT US</span><span>INTRODUCTION</span><span>PROJECT CONTROL</span><span>CONTRACT MANAGEMENT</span><span>SPECIALIST SERVICES</span><span>PROJECTS</span><span>CONTACT US</span>
  </nav>
  <p class="abs copyright">Copyright 2012 Vantrel 4 Management Limited. All rights reserved.</p>
</footer>

</body>
</html>
```